Now Leasing Banner

Looking for a banner that says the following information approx 4' x 30'

Now Leasing Maplewood Terrace 925-318-6054

Target Market(s)

Drive by traffic

Industry/Entity Type

Residential property management

Requirements
Must have
• Clear and readable from a distance

```html
<!DOCTYPE html>
<html lang="en">
<head>
<meta charset="utf-8">
<title>Now Leasing Banner – Maplewood Terrace</title>
<link rel="stylesheet" href="https://fonts.googleapis.com/css2?family=Montserrat:wght@700;800&display=swap">
<style>
  :root {
    --page: #ffffff;
    --navy-deep: #121219;
    --navy-mid: #23233a;
    --navy-tab: #2b2b42;
    --orange: #f7941d;
    --ink: #1a1a2e;
    --white: #ffffff;
    --gold: #c89a5a;
    --sky: #4d9be0;
    --facade: #f3efe7;
  }
  html, body {
    margin: 0;
    width: 1200px;
    height: 769px;
    overflow: hidden;
    background: var(--page);
  }
  .artboard { display: block; width: 1200px; height: 769px; }
  .banner-text { font-family: "Montserrat", "Arial", sans-serif; font-weight: 800; }
  .label-dark { fill: var(--ink); }
  .label-light { fill: var(--white); }
  .label-orange { fill: var(--orange); }
  .ribbon { fill: var(--orange); }
  .corner-tab { fill: var(--navy-tab); }
  .gold-rule { fill: none; stroke: var(--gold); stroke-width: 2.5; }
</style>
</head>
<body>
<svg class="artboard" viewBox="0 0 1200 769" xmlns="http://www.w3.org/2000/svg">
  <defs>
    <linearGradient id="banner-bg" x1="0" y1="0" x2="1" y2="1">
      <stop offset="0" stop-color="#121219"/>
      <stop offset="0.6" stop-color="#23233a"/>
      <stop offset="1" stop-color="#121219"/>
    </linearGradient>
    <radialGradient id="contact-glow" cx="0.3" cy="0.5" r="0.8">
      <stop offset="0" stop-color="#2e2e48"/>
      <stop offset="1" stop-color="#121219"/>
    </radialGradient>
    <linearGradient id="photo-fill" x1="0" y1="0" x2="0" y2="1">
      <stop offset="0" stop-color="#4d9be0"/>
      <stop offset="0.45" stop-color="#a9d0f0"/>
      <stop offset="0.6" stop-color="#f3efe7"/>
      <stop offset="1" stop-color="#e6ded2"/>
    </linearGradient>
  </defs>

  <!-- Banner A: stacked name, contact on the right -->
  <g class="banner banner-stacked">
    <rect x="67" y="202" width="1067" height="142" fill="url(#banner-bg)"/>
    <polygon points="656,202 1134,202 1134,344 660,344 695,272" fill="url(#contact-glow)"/>
    <polyline class="gold-rule" points="656,202 695,272 660,344"/>
    <path class="corner-tab" d="M1067,202 H1134 V245 H1100 Q1088,245 1082,232 Z"/>
    <path class="gold-rule" d="M1067,202 L1082,232 Q1088,245 1100,245 H1134"/>

    <polygon class="ribbon" points="67,215 497,215 512,240 497,265 67,265"/>
    <text class="banner-text label-dark" x="90" y="258" font-size="52" textLength="390" lengthAdjust="spacingAndGlyphs">NOW LEASING</text>
    <text class="banner-text label-light" x="90" y="322" font-size="56" textLength="555" lengthAdjust="spacingAndGlyphs">MAPLEWOOD TERRACE</text>

    <text class="banner-text label-light" x="709" y="257" font-size="33" textLength="289" lengthAdjust="spacingAndGlyphs">CONTACT NOW</text>
    <text class="banner-text label-orange" x="711" y="313" font-size="60" textLength="404" lengthAdjust="spacingAndGlyphs">925-318-6054</text>
  </g>

  <!-- Banner B: two rows with property image panel -->
  <g class="banner banner-with-photo">
    <rect x="68" y="404" width="1067" height="143" fill="url(#banner-bg)"/>
    <polygon points="905,404 1135,404 1135,547 825,547" fill="url(#photo-fill)" role="img" aria-label="Photo of the white apartment building under a blue sky"/>
    <line class="gold-rule" x1="905" y1="404" x2="825" y2="547"/>
    <path class="corner-tab" d="M1075,404 H1135 V445 H1103 Q1091,445 1086,433 Z"/>
    <path class="gold-rule" d="M1075,404 L1086,433 Q1091,445 1103,445 H1135"/>

    <polygon class="ribbon" points="68,425 398,425 409,444 398,464 68,464"/>
    <text class="banner-text label-dark" x="89" y="458" font-size="35" textLength="300" lengthAdjust="spacingAndGlyphs">NOW LEASING</text>
    <text class="banner-text label-light" x="419" y="462" font-size="44" textLength="440" lengthAdjust="spacingAndGlyphs">MAPLEWOOD TERRACE</text>

    <text class="banner-text label-light" x="89" y="517" font-size="33" textLength="289" lengthAdjust="spacingAndGlyphs">CONTACT NOW</text>
    <text class="banner-text label-orange" x="419" y="526" font-size="60" textLength="404" lengthAdjust="spacingAndGlyphs">925-318-6054</text>
  </g>
</svg>
</body>
</html>
```